wealth management firm, professional group, new model

we have a logo that works but we need a card, white background using our colors...clean look

our tag line if can be used in

Steady Counsel For Every Family

```html
<!DOCTYPE html>
<html lang="en">
<head>
<meta charset="utf-8">
<title>Vantor Capital – Business Card</title>
<link rel="stylesheet" href="https://fonts.googleapis.com/css2?family=Montserrat:wght@400;600&display=swap">
<style>
  :root {
    --navy: #1b2d52;
    --rule: #333333;
    --paper: #ffffff;
    --backdrop: #e6e6e6;
  }
  * { box-sizing: border-box; margin: 0; padding: 0; }
  html, body {
    width: 1200px; height: 1200px; overflow: hidden;
    background: var(--backdrop);
    font-family: "Montserrat", sans-serif;
    color: var(--navy);
  }
  .card {
    position: absolute;
    left: 262px;
    width: 718px;
    height: 410px;
    background: var(--paper);
    box-shadow: 0 8px 24px rgba(0,0,0,0.18);
  }
  .card--front { top: 157px; }
  .card--back { top: 675px; }

  .front__brand {
    position: absolute;
    left: 68px; top: 110px;
    font-weight: 600;
    font-size: 30px;
    letter-spacing: 1px;
    color: var(--navy);
  }
  .front__name {
    position: absolute;
    right: 60px; top: 64px;
    font-weight: 600;
    font-size: 26px;
    letter-spacing: 1.5px;
    color: var(--navy);
  }
  .front__divider {
    position: absolute;
    left: 0; right: 0; top: 250px;
    height: 3px;
    background: var(--rule);
  }
  .contact {
    position: absolute;
    top: 293px;
    display: flex; flex-direction: column; gap: 10px;
    list-style: none;
  }
  .contact--left { left: 68px; }
  .contact--right { left: 479px; }
  .contact__item {
    display: flex; align-items: center; gap: 9px;
    font-size: 13.5px; font-weight: 400;
    color: var(--navy);
    height: 21px;
  }
  .contact__icon { width: 21px; height: 21px; flex: none; }

  .back__logo {
    position: absolute;
    left: 0; right: 0; top: 188px;
    display: flex; flex-direction: column; align-items: center;
  }
  .back__brand {
    font-weight: 600;
    font-size: 44px;
    line-height: 1;
    letter-spacing: 1px;
    color: var(--navy);
  }
  .back__tagline {
    margin-top: 20px;
    font-size: 15px; font-weight: 400;
    letter-spacing: 1px;
    color: var(--navy);
  }
</style>
</head>
<body>

<section class="card card--front">
  <div class="front__brand">Vantor Capital</div>
  <div class="front__name">YOUR NAME</div>
  <div class="front__divider"></div>

  <ul class="contact contact--left">
    <li class="contact__item">
      <svg class="contact__icon" viewBox="0 0 20 20" aria-hidden="true">
        <circle cx="10" cy="10" r="10" fill="var(--navy)"/>
        <rect x="4.5" y="5.5" width="11" height="7.5" rx="0.8" fill="none" stroke="#fff" stroke-width="1.2"/>
        <line x1="7.5" y1="15" x2="12.5" y2="15" stroke="#fff" stroke-width="1.2"/>
      </svg>
      yourwebsite.com
    </li>
    <li class="contact__item">
      <svg class="contact__icon" viewBox="0 0 20 20" aria-hidden="true">
        <circle cx="10" cy="10" r="10" fill="var(--navy)"/>
        <path d="M10 15.5 C7 12 6 10.5 6 8.6 A4 4 0 0 1 14 8.6 C14 10.5 13 12 10 15.5Z" fill="#fff"/>
        <circle cx="10" cy="8.6" r="1.5" fill="var(--navy)"/>
      </svg>
      1547 street way , london
    </li>
  </ul>

  <ul class="contact contact--right">
    <li class="contact__item">
      <svg class="contact__icon" viewBox="0 0 20 20" aria-hidden="true">
        <circle cx="10" cy="10" r="10" fill="var(--navy)"/>
        <rect x="6.8" y="4" width="6.4" height="12" rx="1.2" fill="none" stroke="#fff" stroke-width="1.2"/>
        <line x1="9.2" y1="14" x2="10.8" y2="14" stroke="#fff" stroke-width="1"/>
      </svg>
      123 456 789
    </li>
    <li class="contact__item">
      <svg class="contact__icon" viewBox="0 0 20 20" aria-hidden="true">
        <circle cx="10" cy="10" r="10" fill="var(--navy)"/>
        <rect x="4.5" y="6.3" width="11" height="7.6" fill="none" stroke="#fff" stroke-width="1.2"/>
        <polyline points="4.5,6.3 10,10.6 15.5,6.3" fill="none" stroke="#fff" stroke-width="1.2"/>
      </svg>
      youremail@mail.com
    </li>
  </ul>
</section>

<section class="card card--back">
  <div class="back__logo">
    <div class="back__brand">Vantor Capital</div>
    <div class="back__tagline">Steady Counsel For Every Family</div>
  </div>
</section>

</body>
</html>
```